Zanquorra Business Card Design

Zanquorra is a small and new restaurant/ bar location in Hong Kong. The name "Djibouti" derives from an African country. There is no specific reason behind other than the fact, that the bar is somewhat inspired by African elements (only inspired but not purely based on African cuisine etc.).

The bar is somewhat a fusion of African, Mediterranean and Oriental (Old French Vietnam) elements.

However, it is very imperative to stress, that the overall look and feel of Zanquorra is a very high end cocktail lounge/ bar location. The bar is tucked away in a hidden alley, so people will have to know about it. The idea is to send the consumer off in an Escape or hidden remote location where they are at ease in a hip, stylish and trendy environment.

The card needs to feel high-end.

Final logo artwork has been attached and also pictures of the bar/ restaurant itself. The logo ie monkey head cannot be modified. However, the background color and the color of the type "ZANQUORRA" can be changed.

The following details need to fit onto the business card. Of course they can be arranged to your liking:

LOGO

Colin Vey
Partner

+852 97035164
xxx@zanquorra.com
www.zanquorra.com
7C, Brennick Road, Wan Chai, Hong Kong

```html
<!DOCTYPE html>
<html lang="en">
<head>
<meta charset="utf-8">
<title>Zanquorra Business Card Options</title>
<link rel="stylesheet" href="https://fonts.googleapis.com/css2?family=Marcellus+SC&family=Cinzel:wght@700&family=Open+Sans:wght@400;600&display=swap">
<style>
  :root {
    --board: #8b5a36;
    --label: #ffffff;
    --silver-light: #fbfbfb;
    --silver-mid: #e2e2e4;
    --silver-dark: #b9babd;
    --espresso: #231815;
    --mark: #2b1f1b;
    --accent-red: #d3202b;
    --accent-red-dark: #8e1018;
    --card-text: #ffffff;
    --interior-dark: #1c1512;
    --interior-warm: #5a3a28;
    --interior-pink: #7a2a4a;
  }
  * { box-sizing: border-box; margin: 0; padding: 0; }
  html, body { width: 1200px; height: 836px; overflow: hidden; }
  body { background: var(--board); position: relative; font-family: "Open Sans", sans-serif; }

  .option-label {
    position: absolute;
    font-family: "Marcellus SC", serif;
    color: var(--label);
    font-size: 25px;
    letter-spacing: 0.5px;
    transform: translateX(-50%);
    white-space: nowrap;
  }

  .card {
    position: absolute;
    width: 465px;
    height: 265px;
    overflow: hidden;
    box-shadow: 4px 5px 6px rgba(0,0,0,0.45);
    background: linear-gradient(100deg, var(--silver-mid) 0%, var(--silver-light) 30%, var(--silver-mid) 55%, var(--silver-light) 80%, var(--silver-dark) 100%);
  }
  .card svg.card-shapes { position: absolute; inset: 0; }

  .brand-mark {
    position: absolute;
    border-radius: 50%;
    background: var(--mark);
    border: 3px solid #ffffff;
    box-shadow: 0 0 0 2px var(--mark);
  }
  .wordmark {
    position: absolute;
    font-family: "Cinzel", serif;
    font-weight: 700;
    color: var(--espresso);
    white-space: nowrap;
    transform: translateX(-50%);
    letter-spacing: 1px;
  }
  .wordmark--red { color: var(--accent-red); }

  .contact { position: absolute; color: var(--card-text); }
  .contact-name {
    position: absolute;
    right: 0;
    font-size: 17px;
    letter-spacing: 0.5px;
    white-space: nowrap;
  }
  .contact-role {
    position: absolute;
    right: 0;
    font-size: 10px;
    letter-spacing: 1.5px;
    white-space: nowrap;
  }
  .contact-lines { position: absolute; font-size: 10.5px; line-height: 16px; white-space: nowrap; }
  .contact-lines .web { font-weight: 600; font-size: 11px; margin-top: 5px; }
  .contact-lines .address { margin-top: 15px; }

  .interior-photo {
    position: absolute;
    inset: 0;
    background:
      radial-gradient(ellipse at 25% 20%, rgba(220,170,90,0.35), transparent 40%),
      radial-gradient(ellipse at 70% 70%, var(--interior-pink), transparent 55%),
      linear-gradient(180deg, var(--interior-warm) 0%, var(--interior-dark) 100%);
  }
</style>
</head>
<body>

  <div class="option-label" style="left:322px; top:54px;">Front OPTION 1</div>
  <div class="option-label" style="left:888px; top:56px;">BACK OPTION 1</div>
  <div class="option-label" style="left:328px; top:740px;">Front OPTION 2</div>
  <div class="option-label" style="left:880px; top:734px;">BACK OPTION 3</div>

  <!-- Front option 1 -->
  <div class="card card--front-silver" style="left:105px; top:97px;">
    <svg class="card-shapes" width="465" height="265" viewBox="0 0 465 265">
      <defs>
        <linearGradient id="chevron-silver" x1="0" y1="0" x2="1" y2="0">
          <stop offset="0" stop-color="#f2f2f3"/>
          <stop offset="0.6" stop-color="#a9aaad"/>
          <stop offset="1" stop-color="#6f7073"/>
        </linearGradient>
      </defs>
      <polygon points="300,0 325,0 250,130 325,265 300,265 228,130" fill="url(#chevron-silver)"/>
    </svg>
    <div class="interior-photo" role="img" aria-label="Dim lounge interior photograph with warm lamps and wood seating"
         style="clip-path: polygon(325px 0, 465px 0, 465px 265px, 325px 265px, 250px 130px); opacity:0.95;"></div>
    <div class="brand-mark" style="left:66px; top:36px; width:118px; height:118px;"></div>
    <div class="wordmark" style="left:118px; top:154px; font-size:30px;">ZANQUORRA</div>
    <div class="contact" style="left:0; top:0; width:465px; height:265px;">
      <div class="contact-name" style="top:76px; right:25px;">COLIN VEY</div>
      <div class="contact-role" style="top:97px; right:25px;">PARTNER</div>
      <div class="contact-lines" style="left:330px; top:136px;">
        <div>T: +852 97035164</div>
        <div>E: xxx@zanquorra.com</div>
        <div class="web">www.zanquorra.com</div>
        <div class="address">7C, Brennick Road<br>Wan Chai, Hong Kong</div>
      </div>
    </div>
  </div>

  <!-- Back option 1 -->
  <div class="card card--back-photo" style="left:618px; top:93px;">
    <div class="interior-photo" role="img" aria-label="Photograph of the bar interior with pendant lanterns, bottle shelves and pink-lit counter"></div>
  </div>

  <!-- Front option 2 -->
  <div class="card card--front-red" style="left:108px; top:450px;">
    <svg class="card-shapes" width="465" height="265" viewBox="0 0 465 265">
      <defs>
        <linearGradient id="chevron-red" x1="0" y1="0" x2="1" y2="0">
          <stop offset="0" stop-color="var(--accent-red)"/>
          <stop offset="1" stop-color="var(--accent-red-dark)"/>
        </linearGradient>
      </defs>
      <polygon points="297,0 324,0 255,128 324,265 297,265 229,128" fill="url(#chevron-red)"/>
      <polygon points="324,0 465,0 465,265 324,265 255,128" fill="var(--espresso)"/>
    </svg>
    <div class="brand-mark" style="left:70px; top:40px; width:112px; height:112px;"></div>
    <div class="wordmark wordmark--red" style="left:113px; top:152px; font-size:30px;">ZANQUORRA</div>
    <div class="contact" style="left:0; top:0; width:465px; height:265px;">
      <div class="contact-name" style="top:62px; right:25px;">COLIN VEY</div>
      <div class="contact-role" style="top:83px; right:25px;">PARTNER</div>
      <div class="contact-lines" style="left:322px; top:138px;">
        <div>T: +852 97035164</div>
        <div>E: xxx@zanquorra.com</div>
        <div class="web">www.zanquorra.com</div>
        <div class="address">7C, Brennick Road<br>Wan Chai, Hong Kong</div>
      </div>
    </div>
  </div>

  <!-- Back option 3 -->
  <div class="card card--back-silver" style="left:649px; top:450px;">
    <div class="brand-mark" style="left:162px; top:34px; width:124px; height:124px;"></div>
    <div class="wordmark" style="left:232px; top:176px; font-size:35px;">ZANQUORRA</div>
  </div>

</body>
</html>
```